Stationary and document suite for consultancy business in Australia called Lumara

I would like to get a suite of documents suitable for my new business called Lumara. I have included the original brief below, however have already selected a design for the logo. I would like to get:
Letter head - simple letter template with "V" logo embossed in background
Word document - standard format with "V" logo embossed in background
Proposal document - bolder pages with cover and back cover, include empty pages with footer as well as contents
Powerpoint presentation - open to ideas
Email signature - banner style or text, open to ideas
Brief that was given for logo (logo not required)
The name of the business is derived from the latin word for green ("Viridis") combined with "co" which is intended to represent a number of different words: collaborative, cooperative, coaching, collective,  construction, consulting, etc.
My objective for the brand is to represent a dynamic, progressive and collaborative business, where our people have fun and enjoy their work.
The objective of our business is to provide consultancy services to construction businesses, mainly aimed at building high performing teams and strategic growth. We will create learning and development tools that businesses can use to increase staff satisfaction and retention. Our future goal is to invest in decarbonisation and sustainability technology for use in the construction industry.
Our target market is construction business leaders and infrastructure owners, who operate road, rail and utility assets. We also want to present as a dynamic, progressive and fun place to work that will be attractive to new employees.

```html
<!DOCTYPE html>
<html lang="en">
<head>
<meta charset="utf-8">
<title>Lumara – Presentation Template</title>
<link href="https://fonts.googleapis.com/css2?family=Saira+Semi+Condensed:wght@600;700&family=Open+Sans:wght@400;600&family=Poppins:wght@400&display=swap" rel="stylesheet">
<style>
:root{
  --green:#7dc242;
  --charcoal:#4a4a4b;
  --frame:#6b6c6e;
  --grey-text:#7a7b7d;
  --ink:#3a3a3a;
  --stage-dark:#231f20;
  --display:"Saira Semi Condensed","Arial Narrow",sans-serif;
}
*{margin:0;padding:0;box-sizing:border-box}
html,body{width:1200px;height:2255px;overflow:hidden}
body{position:relative;background:var(--stage-dark);font-family:"Open Sans",sans-serif;color:var(--ink)}
.intro{position:absolute;left:0;top:0;width:1200px;height:750px;background:linear-gradient(#cfcfcf,#ececec)}
.intro-title{position:absolute;top:70px;width:100%;text-align:center;font-family:"Poppins",sans-serif;font-weight:400;font-size:25px;letter-spacing:1px;color:#222}
.grid-note{position:absolute;top:790px;width:100%;text-align:center;font-family:"Poppins",sans-serif;font-size:19px;color:#6d6d6d;letter-spacing:.5px}

.slide{position:absolute;width:545px;height:306px;background:linear-gradient(135deg,#ffffff 0%,#eef0ee 45%,#f8f8f8 70%,#e9ebe9 100%);overflow:hidden;box-shadow:0 8px 18px rgba(0,0,0,.45)}
.corner{position:absolute;width:88px;height:88px;border:7px solid var(--frame);z-index:3}
.corner.tl{left:0;top:0;border-right:none;border-bottom:none}
.corner.tr{right:0;top:0;border-left:none;border-bottom:none;border-color:var(--green)}
.corner.bl{left:0;bottom:0;border-right:none;border-top:none}
.corner.br{right:0;bottom:0;border-left:none;border-top:none}
.slide-heading{position:absolute;left:14px;top:20px;font-family:var(--display);font-weight:700;font-size:28px;color:var(--green);letter-spacing:.5px;white-space:nowrap}
.brand-mark{position:absolute;right:16px;top:22px;font-family:var(--display);font-weight:600;font-size:24px;color:var(--grey-text);z-index:4;white-space:nowrap}
.footer-url{position:absolute;left:14px;bottom:9px;font-size:8px;color:#222;z-index:4}
.page-no{position:absolute;right:16px;bottom:9px;font-size:8px;color:#222;z-index:4}

.dark-band{position:absolute;left:0;top:0;width:100%;background:linear-gradient(135deg,#474748,#555557 50%,#444445)}
.white-band{position:absolute;left:0;width:100%;bottom:0;background:#fff}

/* cover */
.cover-photo{position:absolute;left:22px;top:22px;width:158px;height:264px;border:3px solid var(--green);border-radius:6px;background:linear-gradient(160deg,#a87a52,#6b4c35 45%,#2f3540 80%,#3d3a36);z-index:2}
.cover-brand{position:absolute;left:200px;top:48px;width:330px;text-align:center;font-family:var(--display);font-weight:600;font-size:72px;color:#9a9b9d;line-height:1;white-space:nowrap}
.cover-title{position:absolute;left:195px;top:188px;width:340px;text-align:center;font-family:var(--display);font-weight:700;font-size:26px;line-height:1.1;color:var(--green);white-space:nowrap}
.cover-url{position:absolute;left:195px;top:230px;width:340px;text-align:center;font-size:14px;color:#222}

/* about */
.about-copy{position:absolute;left:14px;top:76px;width:262px;font-size:6.3px;line-height:1.55;text-align:justify;color:#333}
.about-copy p+p{margin-top:8px}
.about-photo{position:absolute;left:284px;top:76px;width:250px;height:190px;border:3px solid var(--green);border-radius:6px;background:linear-gradient(160deg,#2f6fc4,#5c95d8 40%,#8aa4b8 70%,#6f6a55)}

/* icon tiles */
.tile{position:absolute;width:66px;height:66px;background:#fff;border-radius:6px;box-shadow:3px 3px 0 var(--green),0 2px 6px rgba(0,0,0,.18);display:flex;align-items:center;justify-content:center}
.tile svg{width:40px;height:40px}
.tile.grey svg{fill:#4d4d4f}
.tile.green svg{fill:var(--green)}
.caption{position:absolute;width:110px;text-align:center;font-family:var(--display);font-weight:600;font-size:9.5px;letter-spacing:.3px;white-space:nowrap}
.caption.green{color:var(--green)}
.caption.grey{color:var(--grey-text)}
.blurb{position:absolute;width:110px;text-align:center;font-size:6.2px;line-height:1.55;color:#333}

.divider-v{position:absolute;width:1px;background:#cfd1cf}
.divider-h{position:absolute;height:1px;background:#cfd1cf}
.hub{position:absolute;width:18px;height:18px;border-radius:50%;background:#77787a;border:3px solid #ddd}

/* timeline */
.mini-tile{position:absolute;width:38px;height:38px;border-radius:5px;background:var(--green);display:flex;align-items:center;justify-content:center}
.mini-tile svg{width:24px;height:24px;fill:#fff}
.timeline{position:absolute;left:14px;right:14px;top:142px;height:1px;background:#d7d9d7}
.step-head{position:absolute;font-family:var(--display);font-weight:700;font-size:9px;color:var(--green);white-space:nowrap}
.step-text{position:absolute;width:76px;font-size:6.2px;line-height:1.6;color:#333}
.step-year{position:absolute;font-family:var(--display);font-weight:600;font-size:13px;color:#c9cac9}

/* donuts */
.donut{position:absolute;width:124px;height:124px}
.donut-label{position:absolute;width:124px;text-align:center;font-family:var(--display);font-weight:700;font-size:28px;line-height:44px;color:#333}
.stat-head{position:absolute;width:150px;text-align:center;font-size:8.5px;font-weight:600;color:var(--green)}
.stat-text{position:absolute;width:150px;text-align:center;font-size:6.3px;line-height:1.6;color:#333}

/* contact */
.contact-brand{position:absolute;left:0;top:46px;width:100%;text-align:center;font-family:var(--display);font-weight:600;font-size:72px;color:#9a9b9d;line-height:1;white-space:nowrap}
.contact-title{position:absolute;left:0;top:183px;width:100%;text-align:center;font-family:var(--display);font-weight:700;font-size:26px;color:var(--green);white-space:nowrap}
.contact-icons{position:absolute;top:225px;left:0;width:100%;display:flex;justify-content:center;gap:10px}
.contact-icons span{width:8px;height:8px;border-radius:50%;background:#333}
.contact-lines{position:absolute;top:240px;left:0;width:100%;text-align:center;font-size:9.5px;line-height:1.6;color:#111}

.closing{position:absolute;left:640px;top:1990px;width:520px;display:flex;align-items:center;justify-content:center;gap:14px}
.closing-brand{font-family:var(--display);font-weight:600;font-size:120px;color:#77787a;line-height:1;white-space:nowrap}
.closing-dot{width:22px;height:22px;background:var(--green);flex:none}
</style>
</head>
<body>

<section class="intro">
  <h1 class="intro-title">POWERPOINT TEMPLATE</h1>

  <article class="slide cover" style="left:327px;top:230px">
    <div class="dark-band" style="height:168px"></div>
    <div class="white-band" style="height:138px"></div>
    <span class="corner tl"></span><span class="corner tr"></span><span class="corner bl"></span><span class="corner br"></span>
    <div class="cover-photo" role="img" aria-label="Photo of a team working on laptops around a wooden table"></div>
    <div class="cover-brand">Lumara</div>
    <div class="cover-title">PRESENTATION TITLE</div>
    <div class="cover-url">www.lumara.com.au</div>
  </article>
</section>

<p class="grid-note">CLICK ZOOM TO SEE DETAILS</p>

<!-- cover -->
<article class="slide cover" style="left:48px;top:862px">
  <div class="dark-band" style="height:168px"></div>
  <div class="white-band" style="height:138px"></div>
  <span class="corner tl"></span><span class="corner tr"></span><span class="corner bl"></span><span class="corner br"></span>
  <div class="cover-photo" role="img" aria-label="Photo of a team working on laptops around a wooden table"></div>
  <div class="cover-brand">Lumara</div>
  <div class="cover-title">PRESENTATION TITLE</div>
  <div class="cover-url">www.lumara.com.au</div>
</article>

<!-- about -->
<article class="slide about" style="left:612px;top:862px">
  <span class="corner tl"></span><span class="corner tr"></span><span class="corner bl"></span><span class="corner br"></span>
  <h2 class="slide-heading">ABOUT US</h2>
  <div class="brand-mark">Lumara</div>
  <div class="about-copy">
    <p>Lorem ipsum dolor sit amet, consectetur adipiscing elit, sed do eiusmod tempor incididunt ut labore et dolore magna aliqua. Ut enim ad minim veniam, quis nostrud exercitation ullamco laboris nisi ut aliquip ex ea commodo consequat. Duis aute irure dolor in reprehenderit in voluptate velit esse cillum dolore eu fugiat nulla pariatur. Excepteur sint occaecat cupidatat non proident, sunt in culpa qui officia deserunt mollit anim id est laborum. Lorem ipsum dolor sit amet, consectetur adipiscing elit, sed do eiusmod tempor incididunt ut labore et dolore magna aliqua.</p>
    <p>Lorem ipsum dolor sit amet, consectetur adipiscing elit, sed do eiusmod tempor incididunt ut labore et dolore magna aliqua. Ut enim ad minim veniam, quis nostrud exercitation ullamco laboris nisi ut aliquip ex ea commodo consequat. Duis aute irure dolor in reprehenderit in voluptate velit esse cillum dolore eu fugiat nulla pariatur. Excepteur sint occaecat cupidatat non proident, sunt in culpa qui officia deserunt mollit anim id est laborum. Lorem ipsum dolor sit amet, consectetur adipiscing elit, sed do eiusmod tempor incididunt ut labore et dolore magna aliqua. Ut enim ad minim veniam, quis nostrud exercitation ullamco laboris nisi ut aliquip ex ea commodo consequat.</p>
  </div>
  <div class="about-photo" role="img" aria-label="Photo of a modern glass office building under a blue sky"></div>
  <span class="footer-url">www.lumara.com.au</span><span class="page-no">01</span>
</article>

<!-- agenda -->
<article class="slide agenda" style="left:48px;top:1205px">
  <div class="dark-band" style="height:168px"></div>
  <div class="white-band" style="height:138px"></div>
  <span class="corner tl"></span><span class="corner tr"></span><span class="corner bl"></span><span class="corner br"></span>
  <h2 class="slide-heading">AGENDA</h2>
  <div class="brand-mark" style="color:#9a9b9d">Lumara</div>

  <div class="tile green" style="left:37px;top:130px"><svg viewBox="0 0 40 40"><rect x="9" y="5" width="22" height="30" rx="2"/><circle cx="20" cy="16" r="4" fill="#fff"/><rect x="13" y="23" width="14" height="6" rx="3" fill="#fff"/></svg></div>
  <div class="tile grey" style="left:172px;top:130px"><svg viewBox="0 0 40 40"><rect x="8" y="4" width="24" height="12" rx="2"/><circle cx="11" cy="22" r="4"/><circle cx="20" cy="20" r="4"/><circle cx="29" cy="22" r="4"/><rect x="5" y="28" width="30" height="8" rx="4"/></svg></div>
  <div class="tile green" style="left:307px;top:130px"><svg viewBox="0 0 40 40"><circle cx="20" cy="13" r="5"/><path d="M11 34a9 9 0 0 1 18 0z"/><rect x="3" y="18" width="8" height="3"/><rect x="29" y="18" width="8" height="3"/><rect x="18.5" y="1" width="3" height="6"/></svg></div>
  <div class="tile grey" style="left:442px;top:130px"><svg viewBox="0 0 40 40"><circle cx="13" cy="20" r="7"/><circle cx="13" cy="20" r="3" fill="#fff"/><rect x="24" y="6" width="10" height="7" rx="1"/><rect x="24" y="17" width="10" height="7" rx="1"/><rect x="24" y="28" width="10" height="7" rx="1"/><rect x="20" y="9" width="2" height="23"/></svg></div>

  <div class="caption green" style="left:15px;top:203px">AGENDA 1</div>
  <div class="caption grey" style="left:150px;top:203px">AGENDA 2</div>
  <div class="caption green" style="left:285px;top:203px">AGENDA 3</div>
  <div class="caption grey" style="left:420px;top:203px">AGENDA 4</div>
  <p class="blurb" style="left:15px;top:218px">Lorem ipsum dolor sit amet, consectetur adipiscing elit, sed do eiusmod tempor incididunt ut labore et dolore magna aliqua.</p>
  <p class="blurb" style="left:150px;top:218px">Lorem ipsum dolor sit amet, consectetur adipiscing elit, sed do eiusmod tempor incididunt ut labore et dolore magna aliqua.</p>
  <p class="blurb" style="left:285px;top:218px">Lorem ipsum dolor sit amet, consectetur adipiscing elit, sed do eiusmod tempor incididunt ut labore et dolore magna aliqua.</p>
  <p class="blurb" style="left:420px;top:218px">Lorem ipsum dolor sit amet, consectetur adipiscing elit, sed do eiusmod tempor incididunt ut labore et dolore magna aliqua.</p>
  <span class="footer-url">www.lumara.com.au</span><span class="page-no">02</span>
</article>

<!-- services -->
<article class="slide services" style="left:612px;top:1205px">
  <span class="corner tl"></span><span class="corner tr"></span><span class="corner bl"></span><span class="corner br"></span>
  <h2 class="slide-heading">SERVICES</h2>
  <div class="brand-mark">Lumara</div>
  <div class="divider-v" style="left:274px;top:78px;height:205px"></div>
  <div class="divider-h" style="left:10px;top:180px;width:525px"></div>
  <div class="hub" style="left:265px;top:171px"></div>

  <div class="tile green" style="left:16px;top:85px"><svg viewBox="0 0 40 40"><circle cx="20" cy="8" r="5"/><rect x="15" y="14" width="10" height="7" rx="2"/><path d="M4 26h10l8 4 12-8 2 3-14 11H10l-6-4z"/></svg></div>
  <div class="tile grey" style="left:170px;top:85px"><svg viewBox="0 0 40 40"><path d="M8 22a12 12 0 0 1 24 0v3h-3v-3a9 9 0 0 0-18 0v3H8z"/><rect x="6" y="21" width="6" height="11" rx="2"/><rect x="28" y="21" width="6" height="11" rx="2"/><circle cx="21" cy="36" r="2.5"/></svg></div>
  <div class="tile green" style="left:311px;top:85px"><svg viewBox="0 0 40 40"><circle cx="20" cy="20" r="15" fill="none" stroke="#7dc242" stroke-width="3" stroke-dasharray="5 3"/><text x="20" y="26" text-anchor="middle" font-family="Saira Semi Condensed,sans-serif" font-weight="700" font-size="15" fill="#7dc242">24</text></svg></div>
  <div class="tile grey" style="left:462px;top:85px"><svg viewBox="0 0 40 40"><circle cx="14" cy="21" r="9"/><circle cx="14" cy="21" r="3.5" fill="#fff"/><rect x="26" y="5" width="6" height="30" rx="2"/><rect x="23" y="5" width="12" height="6" rx="2"/></svg></div>

  <div class="tile green" style="left:16px;top:192px"><svg viewBox="0 0 40 40"><rect x="10" y="5" width="20" height="24" rx="4"/><rect x="13" y="9" width="14" height="7" fill="#fff"/><circle cx="15" cy="23" r="2" fill="#fff"/><circle cx="25" cy="23" r="2" fill="#fff"/><rect x="6" y="32" width="28" height="3"/></svg></div>
  <div class="tile grey" style="left:170px;top:192px"><svg viewBox="0 0 40 40"><path d="M14 5h5l-2 30H6z"/><path d="M21 5h5l8 30H23z"/></svg></div>
  <div class="tile green" style="left:311px;top:192px"><svg viewBox="0 0 40 40"><rect x="5" y="22" width="18" height="8" rx="2"/><rect x="8" y="15" width="9" height="7"/><path d="M17 17l12-10 5 3-2 3-3-1-10 8z"/><rect x="4" y="31" width="21" height="5" rx="2.5"/></svg></div>
  <div class="tile grey" style="left:462px;top:192px"><svg viewBox="0 0 40 40"><path d="M7 30l14-14 3 3-14 14z"/><circle cx="27" cy="12" r="6"/><circle cx="29" cy="10" r="3" fill="#fff"/><path d="M8 8l4-2 20 22-4 4z"/></svg></div>

  <div class="caption green" style="left:-6px;top:164px">SERVICE 1</div>
  <div class="caption grey" style="left:148px;top:164px">SERVICE 2</div>
  <div class="caption green" style="left:289px;top:164px">SERVICE 3</div>
  <div class="caption grey" style="left:440px;top:164px">SERVICE 4</div>
  <div class="caption green" style="left:-6px;top:271px">SERVICE 5</div>
  <div class="caption grey" style="left:148px;top:271px">SERVICE 6</div>
  <div class="caption green" style="left:289px;top:271px">SERVICE 7</div>
  <div class="caption grey" style="left:440px;top:271px">SERVICE 8</div>
  <span class="footer-url">www.lumara.com.au</span><span class="page-no">03</span>
</article>

<!-- infographic timeline -->
<article class="slide timeline-slide" style="left:48px;top:1555px">
  <span class="corner tl"></span><span class="corner tr"></span><span class="corner bl"></span><span class="corner br"></span>
  <h2 class="slide-heading">INFOGRAPHIC</h2>
  <div class="brand-mark">Lumara</div>
  <div class="timeline"></div>
  <div class="divider-v" style="left:96px;top:142px;height:135px"></div>
  <div class="divider-v" style="left:206px;top:142px;height:135px"></div>
  <div class="divider-v" style="left:324px;top:142px;height:135px"></div>
  <div class="divider-v" style="left:434px;top:142px;height:135px"></div>

  <div class="mini-tile" style="left:14px;top:85px"><svg viewBox="0 0 24 24"><rect x="5" y="3" width="10" height="18"/><rect x="15" y="9" width="5" height="12"/><rect x="7" y="6" width="6" height="2" fill="#7dc242"/><rect x="7" y="10" width="6" height="2" fill="#7dc242"/></svg></div>
  <div class="mini-tile" style="left:122px;top:85px"><svg viewBox="0 0 24 24"><circle cx="12" cy="10" r="5"/><rect x="9.5" y="15" width="5" height="5"/><rect x="11" y="1" width="2" height="3"/><rect x="2" y="9" width="3" height="2"/><rect x="19" y="9" width="3" height="2"/></svg></div>
  <div class="mini-tile" style="left:236px;top:85px"><svg viewBox="0 0 24 24"><path d="M20 3c-6 0-10 4-12 9l4 4c5-2 9-6 9-12z"/><path d="M7 14l3 3-5 4-2-2z"/></svg></div>
  <div class="mini-tile" style="left:352px;top:85px"><svg viewBox="0 0 24 24"><circle cx="12" cy="12" r="9" fill="none" stroke="#fff" stroke-width="2"/><circle cx="12" cy="12" r="5" fill="none" stroke="#fff" stroke-width="2"/><circle cx="12" cy="12" r="1.5"/></svg></div>
  <div class="mini-tile" style="left:450px;top:85px"><svg viewBox="0 0 24 24"><rect x="8" y="2" width="8" height="20" rx="2"/><circle cx="12" cy="12" r="5" fill="#fff"/><circle cx="12" cy="12" r="3"/></svg></div>

  <div class="step-head" style="left:14px;top:152px">HEADING 1</div>
  <div class="step-head" style="left:122px;top:152px">HEADING 2</div>
  <div class="step-head" style="left:236px;top:152px">HEADING 3</div>
  <div class="step-head" style="left:352px;top:152px">HEADING 4</div>
  <div class="step-head" style="left:450px;top:152px">HEADING 5</div>
  <p class="step-text" style="left:14px;top:169px">Lorem ipsum dolor sit amet, consectetur adipiscing elit, sed do eiusmod tempor incididunt ut labore et dolore magna aliqua.</p>
  <p class="step-text" style="left:122px;top:169px">Lorem ipsum dolor sit amet, consectetur adipiscing elit, sed do eiusmod tempor incididunt ut labore et dolore magna aliqua.</p>
  <p class="step-text" style="left:236px;top:169px">Lorem ipsum dolor sit amet, consectetur adipiscing elit, sed do eiusmod tempor incididunt ut labore et dolore magna aliqua.</p>
  <p class="step-text" style="left:352px;top:169px">Lorem ipsum dolor sit amet, consectetur adipiscing elit, sed do eiusmod tempor incididunt ut labore et dolore magna aliqua.</p>
  <p class="step-text" style="left:450px;top:169px">Lorem ipsum dolor sit amet, consectetur adipiscing elit, sed do eiusmod tempor incididunt ut labore et dolore magna aliqua.</p>
  <div class="step-year" style="left:14px;top:243px">2010</div>
  <div class="step-year" style="left:122px;top:243px">2013</div>
  <div class="step-year" style="left:236px;top:243px">2016</div>
  <div class="step-year" style="left:352px;top:243px">2019</div>
  <div class="step-year" style="left:450px;top:243px">2022</div>
  <span class="footer-url">www.lumara.com.au</span><span class="page-no">04</span>
</article>

<!-- infographic donuts -->
<article class="slide stats" style="left:612px;top:1555px">
  <span class="corner tl"></span><span class="corner tr"></span><span class="corner bl"></span><span class="corner br"></span>
  <h2 class="slide-heading">INFOGRAPHIC</h2>
  <div class="brand-mark">Lumara</div>

  <svg class="donut" style="left:18px;top:82px" viewBox="0 0 124 124"><circle cx="62" cy="62" r="55" fill="none" stroke="#e3e4e3" stroke-width="12"/><circle cx="62" cy="62" r="55" fill="none" stroke="#7dc242" stroke-width="12" stroke-dasharray="86.4 345.6" transform="rotate(-90 62 62)"/></svg>
  <div class="donut-label" style="left:18px;top:122px">25%</div>
  <svg class="donut" style="left:211px;top:82px" viewBox="0 0 124 124"><circle cx="62" cy="62" r="55" fill="none" stroke="#e3e4e3" stroke-width="12"/><circle cx="62" cy="62" r="55" fill="none" stroke="#7dc242" stroke-width="12" stroke-dasharray="172.8 345.6" transform="rotate(-90 62 62)"/></svg>
  <div class="donut-label" style="left:211px;top:122px">50%</div>
  <svg class="donut" style="left:404px;top:82px" viewBox="0 0 124 124"><circle cx="62" cy="62" r="55" fill="none" stroke="#e3e4e3" stroke-width="12"/><circle cx="62" cy="62" r="55" fill="none" stroke="#7dc242" stroke-width="12" stroke-dasharray="259.2 345.6" transform="rotate(-90 62 62)"/></svg>
  <div class="donut-label" style="left:404px;top:122px">75%</div>

  <div class="stat-head" style="left:5px;top:220px">Lorem ipsum dolor</div>
  <div class="stat-head" style="left:198px;top:220px">Lorem ipsum dolor</div>
  <div class="stat-head" style="left:385px;top:220px">Lorem ipsum dolor</div>
  <p class="stat-text" style="left:5px;top:236px">Lorem ipsum dolor sit amet, consectetur adipiscing elit, sed do eiusmod tempor incididunt ut labore et dolore magna aliqua.</p>
  <p class="stat-text" style="left:198px;top:236px">Lorem ipsum dolor sit amet, consectetur adipiscing elit, sed do eiusmod tempor incididunt ut labore et dolore magna aliqua.</p>
  <p class="stat-text" style="left:385px;top:236px">Lorem ipsum dolor sit amet, consectetur adipiscing elit, sed do eiusmod tempor incididunt ut labore et dolore magna aliqua.</p>
  <span class="footer-url">www.lumara.com.au</span><span class="page-no">05</span>
</article>

<!-- contact -->
<article class="slide contact" style="left:48px;top:1900px">
  <div class="dark-band" style="height:168px"></div>
  <div class="white-band" style="height:138px"></div>
  <span class="corner tl"></span><span class="corner tr"></span><span class="corner bl"></span><span class="corner br"></span>
  <div class="contact-brand">Lumara</div>
  <h2 class="contact-title">CONTACT US</h2>
  <div class="contact-icons"><span></span><span></span><span></span></div>
  <p class="contact-lines">+61 400 555 018<br>hello@lumara.com.au<br>www.lumara.com.au</p>
</article>

<div class="closing">
  <span class="closing-brand">Lumara</span>
  <span class="closing-dot"></span>
</div>

</body>
</html>
```